Commercial Real Estate Marketing Flyer
Property Highlights
Sir,
I(#21) had given the link, from where you can get my PDF file.
Re#3, I like the footer on the upper right/lower left as it takes less space. I am LOVING the watermark on the bottom right! Can we trying placing it behind the upper right/lower left by shrinking the white box? Then I could decide between the footer or the watermark.
Great stuff!
Can we see what it can look like in a 8.5 x 11 portrait format? I like the footer in #1.
Also on the map page, can we supersize the logo like the footer behind the map?
Good work!
what size do you prefer for the flyer? 8.5x11 landscape? Also, I have no problem in sending the file in publisher format--I've worked with publisher plenty of times.
A Great start!!! Setting the bar pretty high!
As a pdf will be fine. Good luck!
OK, I will send the flyer as a PDF - is this OK?
Henry.
I have had requests for photos and text. What I am looking for is a template that I can use repeatedly for different commercial properties. Just use stock photos and garbled text for now.I am looking for a layout that is clean and current.
The template should be made up of "boxes" where I would fill in text, tables and photos. For example page 1 consists of a photo, bullet points and contact info. Page 2 may contain a table for financial info along with more photo boxes.
Page 3 may be photo and text boxes. Page 4 would be maps along with text and table boxes. hope this helps!!
I have had alot of requests that the final be in Adobe Illustrator and not MS Publisher. To all, that is fine. We want to make it easy for everyone. We will deal with it later. So... go for it!!
Hi, send the text and logo youd like si I can draft up for you thanks...
Please give me your details.Also send me images,texts and other materials that you want to use on your flyer So that I can prepare the Flyer Design for you.
Faris Okoth
Sir I prepare the require design in Adobe Illustrator and if I get success the final file I will provide you in .pdf format. Sir if it is OK then I go a head. Because don't use MS Publisher
Thanks & Regards
Deepak Ruvari
You can see samples of the flyers uploaded in the "Read Brief" section. Good Luck!
please send link of the flyer. Thanks!
Please take a look at the samples we have uploaded along with our new Logo (thanks to IconBrio!). It must be compatible to using MS Publisher. If you want examples of flyers that we like, please private message me and I will link a few flyers.

```html
<!DOCTYPE html>
<html lang="en">
<head>
<meta charset="utf-8">
<title>Northgate Realty – Property Flyer</title>
<link href="https://fonts.googleapis.com/css2?family=Open+Sans:wght@400;600;700&family=Great+Vibes&display=swap" rel="stylesheet">
<style>
:root{
  --navy:#142a63;
  --blue:#24479a;
  --sky:#3f6cc4;
  --ink:#333;
  --muted:#777;
  --rule:#d5d9e3;
  --paper:#ffffff;
  --bg:#e7e4df;
}
*{box-sizing:border-box;margin:0;padding:0}
html,body{width:1200px;height:866px;overflow:hidden;background:var(--bg);font-family:"Open Sans",Arial,sans-serif;color:var(--ink)}
.sheet{position:absolute;width:490px;height:380px;background:var(--paper);box-shadow:0 3px 10px rgba(0,0,0,.25);overflow:hidden}
.sheet--cover{left:80px;top:70px}
.sheet--summary{left:610px;top:70px}
.sheet--market{left:80px;top:470px}
.sheet--map{left:610px;top:470px;background:var(--navy)}
.brand{display:flex;align-items:center;gap:6px}
.brand__dot{width:26px;height:26px;border-radius:50%;background:var(--blue)}
.brand__name{font-weight:700;font-size:15px;color:var(--navy)}
.cover__head{height:62px;display:flex;justify-content:space-between;align-items:center;padding:0 16px}
.cover__addr{font-size:6.5px;line-height:1.5;color:var(--muted);text-align:left}
.cover__addr b{color:var(--navy)}
.photo{display:block}
.cover__photo{height:240px;background:linear-gradient(180deg,#9fc1e3 0%,#c9dcec 35%,#8da77a 60%,#5f7d4a 100%)}
.cover__caption{height:42px;background:var(--navy);color:#fff;font-size:7.5px;line-height:1.5;padding:8px 16px}
.cover__foot{height:36px;display:flex;align-items:center;justify-content:space-between;padding-left:16px}
.site{font-size:10px;color:var(--navy);font-weight:600}
.cover__corner{width:170px;height:36px;background:linear-gradient(100deg,var(--paper) 0 18%,var(--sky) 18%,var(--navy))}
.tab{display:inline-flex;align-items:center;gap:6px;background:var(--blue);color:#fff;font-weight:700;font-size:12px;padding:6px 14px 6px 10px;margin-top:14px;border-radius:0 14px 14px 0}
.tab i{width:14px;height:14px;border-radius:50%;background:#fff;display:block}
.summary__title{font-family:"Great Vibes",cursive;font-size:26px;color:var(--navy);padding:4px 16px 0}
.summary__intro{font-size:6px;line-height:1.5;color:var(--muted);padding:2px 16px 8px}
.summary__tables{display:flex;gap:10px;padding:0 16px}
table{border-collapse:collapse;font-size:5.5px}
td,th{padding:1.6px 3px;border-bottom:1px solid var(--rule);text-align:left}
.facts{width:125px}
.facts td:last-child{text-align:right}
.units{flex:1}
.units th{background:var(--navy);color:#fff;font-weight:600}
.units td{text-align:right}
.units td:first-child{text-align:left}
.units tr.total td{font-weight:700;background:#eef1f7}
.band{position:absolute;left:0;right:0;bottom:0;height:34px;background:linear-gradient(90deg,var(--navy),var(--sky));display:flex;align-items:center;padding-left:16px}
.band .site{color:#fff}
.market__body{display:flex;gap:12px;padding:10px 16px 0}
.market__photos{width:96px;display:flex;flex-direction:column;gap:6px}
.market__photos .photo{height:82px;background:linear-gradient(180deg,#b7cbe0,#8a8f86)}
.market__text{flex:1;font-size:6px;line-height:1.55;color:var(--muted)}
.market__text p{margin-bottom:6px}
.market__text b{color:var(--blue)}
.map__head{height:54px;display:flex;align-items:center;padding-left:18px}
.map__head .brand__name{color:#fff}
.map__head .brand__dot{background:var(--sky)}
.map__area{position:relative;height:262px;margin:0 18px;background:linear-gradient(135deg,#e9dfc4,#d8cfb3)}
.map__list{position:absolute;left:8px;top:8px;width:150px;background:rgba(255,255,255,.92);font-size:6px;line-height:1.7;padding:6px 8px;list-style:none;counter-reset:n}
.map__list li{counter-increment:n}
.map__list li::before{content:counter(n) ". ";color:var(--blue);font-weight:700}
.map__foot{text-align:center;color:#fff;padding-top:12px}
.map__foot .name{font-size:8px;font-weight:700;letter-spacing:.5px}
.map__foot .addr{font-size:7px;margin-top:5px}
</style>
</head>
<body>

<section class="sheet sheet--cover">
  <header class="cover__head">
    <div class="brand"><span class="brand__dot"></span><span class="brand__name">Northgate</span></div>
    <div class="cover__addr"><b>NORTHGATE REALTY</b><br>218 W Linden Ave, Suite 400<br>Maple Grove, CA 95410</div>
  </header>
  <div class="photo cover__photo" role="img" aria-label="Photo of the apartment property with lawn, trees and entry sign"></div>
  <p class="cover__caption">Northgate Realty possesses immense depth of knowledge of the multi-family housing market, due to their extensive experience as brokers, owners and buyers of apartments.</p>
  <footer class="cover__foot"><span class="site">www.northgaterealty.com</span><span class="cover__corner"></span></footer>
</section>

<section class="sheet sheet--summary">
  <div class="tab"><i></i>Investment Summary</div>
  <h2 class="summary__title">The Willows</h2>
  <p class="summary__intro">Lorem ipsum dolor sit amet consectetur adipiscing elit, sed do eiusmod tempor incididunt ut labore et dolore magna aliqua. Ut enim ad minim veniam quis nostrud exercitation ullamco laboris nisi ut aliquip ex ea commodo consequat duis aute irure dolor in reprehenderit in voluptate velit esse cillum dolore eu fugiat.</p>
  <div class="summary__tables">
    <table class="facts">
      <tr><td>Offering Price</td><td>$4,250,000</td></tr>
      <tr><td>Units</td><td>48</td></tr>
      <tr><td>Price / Unit</td><td>$88,541</td></tr>
      <tr><td>Price / SF</td><td>$92</td></tr>
      <tr><td>Current GRM</td><td>7.45</td></tr>
      <tr><td>Market GRM</td><td>6.80</td></tr>
      <tr><td>Current Cap Rate</td><td>7.1%</td></tr>
      <tr><td>Market Cap Rate</td><td>7.9%</td></tr>
      <tr><td>Year Built</td><td>1984</td></tr>
      <tr><td>Lot Size</td><td>2.1 Acres</td></tr>
      <tr><td>Gross SF</td><td>46,200</td></tr>
      <tr><td>Parking</td><td>Covered</td></tr>
    </table>
    <table class="units">
      <tr><th>Unit Type</th><th>Units</th><th>Sq Ft</th><th>Rent</th><th>Total</th><th>Market</th><th>Total</th></tr>
      <tr><td>1 Bed / 1 Bath</td><td>12</td><td>650</td><td>$695</td><td>$8,340</td><td>$750</td><td>$9,000</td></tr>
      <tr><td>2 Bed / 1 Bath</td><td>16</td><td>850</td><td>$795</td><td>$12,720</td><td>$850</td><td>$13,600</td></tr>
      <tr><td>2 Bed / 2 Bath</td><td>12</td><td>950</td><td>$845</td><td>$10,140</td><td>$900</td><td>$10,800</td></tr>
      <tr><td>3 Bed / 2 Bath</td><td>8</td><td>1,150</td><td>$995</td><td>$7,960</td><td>$1,050</td><td>$8,400</td></tr>
      <tr class="total"><td>Total</td><td>48</td><td>41,200</td><td></td><td>$39,160</td><td></td><td>$41,800</td></tr>
    </table>
  </div>
  <div class="band"></div>
</section>

<section class="sheet sheet--market">
  <div class="tab"><i></i>Market Overview</div>
  <div class="market__body">
    <div class="market__photos">
      <div class="photo" role="img" aria-label="Photo of a downtown office building"></div>
      <div class="photo" role="img" aria-label="Photo of a shopping center"></div>
      <div class="photo" role="img" aria-label="Photo of a residential street"></div>
    </div>
    <div class="market__text">
      <p><b>POPULATION:</b> Lorem ipsum dolor sit amet consectetur adipiscing elit sed do eiusmod tempor incididunt ut labore et dolore magna aliqua ut enim ad minim veniam quis nostrud exercitation.</p>
      <p><b>THE ECONOMY:</b> Duis aute irure dolor in reprehenderit in voluptate velit esse cillum dolore eu fugiat nulla pariatur excepteur sint occaecat cupidatat non proident sunt in culpa qui officia.</p>
      <p><b>GOVERNMENT INITIATIVES:</b> Sed ut perspiciatis unde omnis iste natus error sit voluptatem accusantium doloremque laudantium totam rem aperiam eaque ipsa quae ab illo inventore.</p>
      <p><b>RECREATION:</b> Nemo enim ipsam voluptatem quia voluptas sit aspernatur aut odit aut fugit sed quia consequuntur magni dolores eos qui ratione voluptatem sequi nesciunt neque porro quisquam.</p>
    </div>
  </div>
  <div class="band"><span class="site">www.northgaterealty.com</span></div>
</section>

<section class="sheet sheet--map">
  <header class="map__head">
    <div class="brand"><span class="brand__dot"></span><span class="brand__name">Northgate</span></div>
  </header>
  <div class="map__area" role="img" aria-label="Street map of the area around the property">
    <ol class="map__list">
      <li>Linden Street Health Center</li>
      <li>High School</li>
      <li>Elementary School</li>
      <li>Central Library Branch</li>
      <li>Riverside Shopping Plaza</li>
      <li>Community Park</li>
      <li>Medical Office Center</li>
      <li>Maple Grove College</li>
      <li>Grocery Market</li>
      <li>Freeway Access</li>
    </ol>
  </div>
  <footer class="map__foot">
    <div class="name">NORTHGATE REALTY</div>
    <div class="addr">218 W Linden Ave, Suite 400, Maple Grove, CA 95410 &nbsp; Phone 555-210-4400 &nbsp; Fax 555-210-4411</div>
  </footer>
</section>

</body>
</html>
```